A Training Firm needs a Brochure - Clearpath Onboarding Skills Brochure

Brevaloom, a HR Consulting Firm focused on Training & Development is seeking a Brochure Design for one of its training programs - Clearpath Onboarding Skills Program.

The designs should be innovative,image led and interesting to read. We would like to see designs that incorporate the colours Blue and Green. Because this company is based in Africa, we would like the designers to use image of Black people instead of Caucasians.

Brevaloom is a member of Tandrel Group, a HR Consulting firm that offers services in the area of Learning, Talent Solutions, Outsourcing and Strategy Consulting

Target Market(s)

CEOs, HR Directors, Heads of Learning and Learning Managers of Large, Medium and Small Scale Organisations in Nigeria

Industry/Entity Type

Training

Other font styles liked:
• Corbel

Colors
3176b5
abd036

Requirements
Must have
• Brevaloom Logo, A link with the Parent Company Tandrel Group (We usually add that Brevaloom is a member of the Tandrel Group) The Group Logo and the Pantone Colours have been attached
Nice to have
• The entire Brochure should be graphically led. That is, lots of graphics - Infographics/Images/colours etc
Should not have
• No Caucasian images. We are an African based Firm and would like to have African images

```html
<!DOCTYPE html>
<html lang="en">
<head>
<meta charset="utf-8">
<title>Clearpath Onboarding Skills Brochure – Brevaloom</title>
<link href="https://fonts.googleapis.com/css2?family=Open+Sans:wght@400;600;700&display=swap" rel="stylesheet">
<style>
  :root{
    --stage:#e4e4e4;
    --olive:#a9ba6e;
    --olive-light:#c9d69c;
    --olive-dark:#585d37;
    --olive-darker:#44482b;
    --slate:#6b7262;
    --teal:#2a7f85;
    --teal-deep:#1c6e7e;
    --teal-bright:#2a93a0;
    --navy-teal:#1e4c5c;
    --mint:#8ec59e;
    --lime:#abd036;
    --white:#ffffff;
  }
  *{box-sizing:border-box;margin:0;padding:0}
  html,body{width:1200px;height:860px;overflow:hidden}
  body{background:var(--stage);font-family:"Open Sans",sans-serif;color:var(--white)}
  .spread{position:absolute;left:40px;top:40px;width:1120px;height:780px;display:flex;box-shadow:0 10px 30px rgba(0,0,0,.18)}
  .page{position:relative;width:560px;height:780px;overflow:hidden}

  /* left page */
  .page--left{background:var(--olive)}
  .page--left .frame{position:absolute;left:16px;top:16px;right:16px;bottom:58px;background:var(--olive-light)}
  .programme-table{position:absolute;left:30px;top:28px;width:490px;display:flex;flex-direction:column;gap:6px}
  .row{display:grid;grid-template-columns:28px 150px 1fr;min-height:226px}
  .row__num{font-size:10px;font-weight:600;padding:10px 0 0 9px}
  .row__title{font-size:13px;font-weight:700;line-height:1.3;padding:12px 12px}
  .row__desc{font-size:8.6px;line-height:1.5;padding:10px 14px}
  .row__desc p+p{margin-top:7px}

  .page--left .row__num{background:var(--slate)}
  .page--left .row__title{background:var(--teal)}
  .page--left .row__desc{background:linear-gradient(160deg,var(--olive-dark),var(--olive-darker))}

  .footer-left{position:absolute;left:0;bottom:16px;width:100%;height:26px;display:flex;align-items:center}
  .footer-left .page-num{width:26px;height:26px;background:var(--teal);color:var(--white);font-weight:700;font-size:13px;display:flex;align-items:center;justify-content:center;margin-left:16px}
  .footer-left .running-title{font-size:15px;font-weight:600;color:var(--teal);margin-left:10px}

  /* right page */
  .page--right{background:linear-gradient(135deg,var(--teal-bright),var(--teal-deep))}
  .page--right .programme-table{left:24px;top:18px;width:500px}
  .page--right .row__num{background:var(--teal-deep)}
  .page--right .row__title{background:linear-gradient(180deg,var(--mint),#5fa79a)}
  .page--right .row__desc{background:var(--navy-teal)}
  .page--right .row--lead{min-height:60px}
  .page--right .row--lead .row__num,.page--right .row--lead .row__title{background:transparent}
  .page--right .row--lead .row__title{background:linear-gradient(180deg,#9fd0a8,var(--mint))}
  .page--right .row{min-height:214px}
  .page--right .row.row--lead{min-height:58px}

  .footer-right{position:absolute;right:22px;bottom:22px;display:flex;align-items:center;gap:8px}
  .footer-right .brand{font-size:14px;font-weight:700;color:var(--white)}
  .footer-right .page-num{width:22px;height:22px;background:var(--lime);color:var(--teal-deep);font-weight:700;font-size:12px;display:flex;align-items:center;justify-content:center}

  .gutter{position:absolute;left:558px;top:0;width:4px;height:780px;background:linear-gradient(90deg,rgba(0,0,0,.18),rgba(0,0,0,0))}
</style>
</head>
<body>
<div class="spread">
  <section class="page page--left">
    <div class="frame"></div>
    <div class="programme-table">
      <article class="row">
        <div class="row__num">3</div>
        <h2 class="row__title">Workplace Effectiveness &amp; Productivity</h2>
        <div class="row__desc">
          <p>Organisations that have excelled and redefined excellence in their industries thrive on the high performance standards delivered by individual contributors. These people have mastered the rules of work and have perfected habits that produce excellence in their work.</p>
          <p>This course explores comprehensive and proven sets of professional skills that help participants achieve focus, develop personal mastery and work effectively with colleagues and build a reputation for results.</p>
          <p>It is designed to help participants develop the right blend of professional skills and habits that drive personal and organisational productivity, while meeting the expectations of the business environment.</p>
        </div>
      </article>
      <article class="row">
        <div class="row__num">4</div>
        <h2 class="row__title">The Internal Consultant Programme</h2>
        <div class="row__desc">
          <p>The consultant is a problem solver and change agent. Internal consultants support business units by diagnosing issues, proposing solutions and guiding implementation with discipline and care.</p>
          <p>This programme is designed to develop practical skills required in the consulting process. It introduces the tools and techniques used to collaborate with internal clients and add lasting value.</p>
          <p>While acquainting participants with their role as problem solvers, the course breaks down the stages of consulting: entry, contracting, diagnosis, feedback, implementation and closure.</p>
          <p>Guided by thorough case discussions, participants will simulate consulting engagements and learn how to sustain credibility with stakeholders.</p>
        </div>
      </article>
      <article class="row">
        <div class="row__num">5</div>
        <h2 class="row__title">Introduction to Strategic Thinking &amp; Execution Programme</h2>
        <div class="row__desc">
          <p>Every successful business must have individuals who understand strategy and who are able to convert it into results. It is one thing to plan well and another thing to execute with consistency.</p>
          <p>Execution is the ability to get things done, deliver on tasks and provide quality work aligned with organisational goals. Good strategies fail when execution is weak.</p>
          <p>This course introduces participants to the principles of strategic thinking and execution, equipping them with tools to translate objectives into action while maximising available resources.</p>
        </div>
      </article>
    </div>
    <footer class="footer-left">
      <span class="page-num">4</span>
      <span class="running-title">Clearpath Onboarding Programmes</span>
    </footer>
  </section>

  <section class="page page--right">
    <div class="programme-table">
      <article class="row row--lead">
        <div class="row__num"></div>
        <div class="row__title"></div>
        <div class="row__desc">
          <p>It will provide an overall view of the environment in which your organisation operates and the implications of various events on your business.</p>
        </div>
      </article>
      <article class="row">
        <div class="row__num">6</div>
        <h2 class="row__title">Working Effectively in a Team</h2>
        <div class="row__desc">
          <p>Self-directed work teams are the cornerstone of high performance organisations. Teams markedly outperform individuals when roles are clear and goals are shared.</p>
          <p>Work teams were among the most popular workplace innovations of the last decade, and leading organisations count teamwork as critical to their success.</p>
          <p>To work together, team members must develop their interactive, communication and interpersonal skills. This course builds collaboration, trust and healthy problem solving.</p>
          <p>This workshop focuses on crucial interpersonal skills that team members must have if they are to function as a high performance unit.</p>
        </div>
      </article>
      <article class="row">
        <div class="row__num">7</div>
        <h2 class="row__title">Developing a Customer Service Mind-set</h2>
        <div class="row__desc">
          <p>Service is first and foremost a mind-set. Creating a customer focused mind-set and delivering a level of service that consistently wows customers will set an organisation apart in a competitive market.</p>
          <p>Designed to instil the necessary behaviours and customer service commitment in new hires, this course builds a customer-centric attitude and a clear view of the customer value chain.</p>
        </div>
      </article>
      <article class="row">
        <div class="row__num">8</div>
        <h2 class="row__title">Strategies for Building and Managing Relationships</h2>
        <div class="row__desc">
          <p>When employees join a new organisation, the ease of adapting to a new environment and the results they achieve depend largely on the ability to build productive relationships.</p>
          <p>The individual is responsible for fostering outstanding working relationships with supervisors, peers and subordinates within the organisation.</p>
          <p>This course gives new hires insights into developing mutually rewarding relationships, with skills for communicating and managing expectations at work.</p>
          <p>Trends and developments in the world of work will be brought into perspective and evaluated as the cornerstone of effective working relationships.</p>
        </div>
      </article>
    </div>
    <footer class="footer-right">
      <span class="brand">brevaloom</span>
      <span class="page-num">5</span>
    </footer>
  </section>
  <div class="gutter"></div>
</div>
</body>
</html>
```